PAWS postcard design

We need a design for a non profit organization associated with an animal shelter called PAWS of HBRPC. HBRPC stands for Hollybrook Valley Regional Pet Center. This 501c3 group provides assistance to the community in the form of training, consultation, financial assistance, education and more. Our goal is to provide options to people in need to help them keep their pets rather than surrender them to the shelter. We have a logo already but we need something for people to take away and to use as a handout. Need to include phone numbers and website, which I will provide.

Target Market(s)

general public who have pets

Industry/Entity Type

Non Profit

Font styles to use
Sans Serif
Other font styles liked:
• designer can choose others

Requirements
Must have
• The logo must be fairly large. Colors should be bright and eye-pleasing. Like colors that match the logo. Easy to read fonts. Pics of animals are OK but no pics with people. Not too much text, short and to the point.
Nice to have
• not sure
Should not have
• No pics with people. Not black and white. Not too much text.

```html
<!DOCTYPE html>
<html lang="en">
<head>
<meta charset="utf-8">
<title>PAWS of HBRPC Postcard</title>
<link rel="stylesheet" href="https://fonts.googleapis.com/css2?family=Arvo:wght@700&family=Open+Sans:wght@400&family=Arimo:wght@400;700&family=Roboto+Condensed:wght@400;700&display=swap">
<style>
  :root {
    --card-yellow: #f3e16e;
    --headline-red: #d3473a;
    --band-red: #d14b32;
    --brand-blue: #22c0ea;
    --ink: #141414;
    --paw-green: #8ea86c;
    --white: #ffffff;
    --social-blue: #1e8fe3;
    --photo-light: #d9a068;
    --photo-dark: #a4662f;
  }
  * { margin: 0; padding: 0; box-sizing: border-box; }
  html, body { width: 1200px; height: 673px; overflow: hidden; background: #e8e5e0; }
  .postcard {
    position: relative;
    width: 1200px;
    height: 673px;
    background: var(--card-yellow);
    overflow: hidden;
  }
  .headline {
    position: absolute;
    left: 51px;
    top: 50px;
    font-family: "Arvo", Georgia, serif;
    font-weight: 700;
    font-size: 50px;
    line-height: 62px;
    color: var(--headline-red);
    letter-spacing: -0.5px;
    z-index: 2;
  }
  .goal {
    position: absolute;
    left: 51px;
    top: 173px;
    font-family: "Open Sans", Arial, sans-serif;
    font-size: 31px;
    color: var(--ink);
    z-index: 2;
  }
  .services {
    position: absolute;
    left: 54px;
    top: 262px;
    font-family: "Arimo", Arial, sans-serif;
    color: var(--ink);
  }
  .services-intro { font-size: 19.5px; margin-bottom: 8px; }
  .services-list { list-style: none; }
  .services-list li {
    display: flex;
    align-items: center;
    gap: 13px;
    font-size: 20.5px;
    height: 32.5px;
  }
  .paw { width: 24px; height: 22px; flex: none; color: var(--paw-green); }
  .photo {
    position: absolute;
    left: 690px;
    top: 0;
    width: 510px;
    height: 673px;
    background: radial-gradient(ellipse at 62% 48%, var(--photo-light) 0%, var(--photo-dark) 60%, #eee6dc 100%);
    clip-path: polygon(127px 0, 100% 0, 100% 100%, 156px 100%, 156px 466px, 127px 366px, 0 260px, 20px 187px);
    z-index: 1;
  }
  .contact-band {
    position: absolute;
    left: 0;
    top: 466px;
    width: 846px;
    height: 207px;
    background: var(--band-red);
  }
  .brand-block {
    position: absolute;
    left: 0;
    top: 0;
    width: 192px;
    height: 207px;
    background: var(--brand-blue);
    display: flex;
    align-items: center;
    justify-content: center;
  }
  .brand-name {
    font-family: "Roboto Condensed", Arial, sans-serif;
    font-weight: 700;
    font-size: 24px;
    color: var(--white);
  }
  .contact-details {
    position: absolute;
    left: 192px;
    top: 0;
    width: 540px;
    height: 207px;
    text-align: center;
    color: var(--white);
    padding-top: 21px;
  }
  .cta {
    font-family: "Roboto Condensed", Arial, sans-serif;
    font-size: 26px;
    line-height: 34px;
  }
  .phone {
    display: flex;
    justify-content: center;
    align-items: center;
    gap: 14px;
    font-family: "Arimo", Arial, sans-serif;
    font-size: 33px;
    line-height: 48px;
    margin-top: 2px;
  }
  .phone svg { width: 36px; height: 36px; }
  .website {
    font-family: "Arimo", Arial, sans-serif;
    font-weight: 700;
    font-size: 26px;
    letter-spacing: 1.5px;
    line-height: 40px;
  }
  .shelter-name {
    font-family: "Roboto Condensed", Arial, sans-serif;
    font-weight: 700;
    font-size: 23px;
    line-height: 34px;
  }
  .social-dot {
    position: absolute;
    left: 791px;
    top: 19px;
    width: 48px;
    height: 48px;
    border-radius: 50%;
    background: var(--social-blue);
  }
</style>
</head>
<body>
<svg width="0" height="0" style="position:absolute">
  <defs>
    <symbol id="paw-icon" viewBox="0 0 24 22">
      <ellipse cx="5" cy="6" rx="2.6" ry="3.2" fill="currentColor"/>
      <ellipse cx="10" cy="3.5" rx="2.6" ry="3.2" fill="currentColor"/>
      <ellipse cx="16" cy="4" rx="2.6" ry="3.2" fill="currentColor"/>
      <ellipse cx="20.5" cy="8.5" rx="2.4" ry="3" fill="currentColor"/>
      <ellipse cx="12.5" cy="15" rx="6" ry="5.5" fill="currentColor"/>
    </symbol>
  </defs>
</svg>
<main class="postcard">
  <h1 class="headline">THERE IS A WAY TO KEEP<br>YOUR LOVING ANIMAL</h1>
  <p class="goal">Our goal is to provide options to help you!</p>

  <section class="services">
    <p class="services-intro">We provide assistance to the community in the form of:</p>
    <ul class="services-list">
      <li><svg class="paw"><use href="#paw-icon"/></svg>TRAINING</li>
      <li><svg class="paw"><use href="#paw-icon"/></svg>CONSULTATION</li>
      <li><svg class="paw"><use href="#paw-icon"/></svg>FINANCIAL ASSISTANCE</li>
      <li><svg class="paw"><use href="#paw-icon"/></svg>EDUCATION</li>
      <li><svg class="paw"><use href="#paw-icon"/></svg>AND MORE.</li>
    </ul>
  </section>

  <footer class="contact-band">
    <div class="brand-block">
      <span class="brand-name">PAWS of HBRPC</span>
    </div>
    <div class="contact-details">
      <p class="cta">FREE CONSULTATION, GET HELP TODAY</p>
      <p class="phone">
        <svg viewBox="0 0 36 36" aria-hidden="true">
          <circle cx="18" cy="18" r="16" fill="none" stroke="#fff" stroke-width="2.5"/>
          <path d="M12.5 10.5c1-.8 2-.6 2.6.3l1.6 2.6c.5.8.3 1.7-.4 2.2l-1 .8c.9 2 2.4 3.6 4.4 4.6l.8-1c.6-.7 1.5-.9 2.2-.4l2.6 1.6c.9.6 1.1 1.7.3 2.6l-1.2 1.3c-1 1-2.6 1.2-4 .5-4.4-2.1-7.8-5.5-9.8-9.9-.6-1.4-.3-3 .7-4z" fill="#fff"/>
        </svg>
        555-204-7319
      </p>
      <p class="website">www.pawsofhbrpc.org</p>
      <p class="shelter-name">Hollybrook Valley Regional Pet Center</p>
    </div>
    <span class="social-dot" aria-label="Social media"></span>
  </footer>

  <div class="photo" role="img" aria-label="Photo of a tan and white puppy with floppy ears looking at the viewer"></div>
</main>
</body>
</html>
```